Maple Burrow Canine Massage Needs a Business Card Design

Maple Burrow Canine Massage is a new therapeutic canine massage company located in Nederland, Colorado. I need a business card design that include my logo and basic contact information.

Target Market(s)

Pet owners, veterinarians

Industry/Entity Type

Business

Contact Information for Business Card

Tessa Lindqvist, CCMT
303.581.7296
tessa@mapleburrowmassage.example
www.mapleburrowmassage.example

Colors
6c459b
886aae
b8a6cd
a64599
b768aa
d3a5cc
fbed22

Requirements
Must have
• Font should be similar to font in logo.

```html
<!DOCTYPE html>
<html lang="en">
<head>
<meta charset="utf-8">
<title>Maple Burrow Canine Massage – Business Card</title>
<link rel="stylesheet" href="https://fonts.googleapis.com/css2?family=Source+Sans+3:wght@400;600&display=swap">
<style>
  :root {
    --stage: #595957;
    --card: #f5f5f5;
    --watermark: #e7e5ee;
    --purple-deep: #6c459b;
    --purple-mid: #886aae;
    --orchid: #b768aa;
    --lilac: #b584bb;
  }
  * { margin: 0; padding: 0; box-sizing: border-box; }
  html, body {
    width: 1200px;
    height: 782px;
    overflow: hidden;
    background: var(--stage);
    font-family: "Source Sans 3", "Myriad Pro", Arial, sans-serif;
  }
  .card {
    position: absolute;
    left: 111px;
    top: 110px;
    width: 979px;
    height: 565px;
    background: var(--card);
    overflow: hidden;
  }
  .card__watermark {
    position: absolute;
    left: -40px;
    top: 60px;
    width: 620px;
    height: 560px;
    background: radial-gradient(ellipse 48% 50% at 55% 55%, var(--watermark) 0%, var(--watermark) 60%, rgba(231,229,238,0) 100%);
  }
  .brand {
    position: absolute;
    left: 50px;
    top: 400px;
    width: 210px;
    display: flex;
    flex-direction: column;
    align-items: center;
    gap: 12px;
  }
  .brand__dot {
    width: 72px;
    height: 72px;
    border-radius: 50%;
    background: var(--lilac);
  }
  .brand__name {
    color: var(--purple-deep);
    font-weight: 600;
    font-size: 20px;
    line-height: 1.15;
    text-align: center;
  }
  .contact {
    position: absolute;
    left: 480px;
    top: 272px;
    color: var(--purple-mid);
    white-space: nowrap;
  }
  .contact__name {
    color: var(--purple-deep);
    font-weight: 600;
    font-size: 30px;
    line-height: 1;
  }
  .contact__title {
    margin-top: 36px;
    color: var(--orchid);
    font-size: 29px;
    line-height: 1;
  }
  .contact__lines {
    margin-top: 32px;
    font-size: 28px;
    line-height: 40px;
    list-style: none;
  }
</style>
</head>
<body>
  <main class="card">
    <div class="card__watermark" role="img" aria-label="Large faint silhouette illustration of two dogs"></div>

    <div class="brand">
      <span class="brand__dot"></span>
      <span class="brand__name">Maple Burrow Canine Massage</span>
    </div>

    <section class="contact">
      <h1 class="contact__name">Tessa Lindqvist</h1>
      <p class="contact__title">CCMT</p>
      <ul class="contact__lines">
        <li>303.581.7296</li>
        <li>tessa@mapleburrowmassage.example</li>
        <li>www.mapleburrowmassage.example</li>
      </ul>
    </section>
  </main>
</body>
</html>
```